KESTREL Communications Business Card- Belsa

Kestrel Integrated Communications is Corporate communications agency with more than 20 years of experience. We become part of the manegement team of our clients in other to improve their outcomes and grow the possitioning of their brand.
We are in Puerto Rico, latin caribbean island
Name: Maribelsa (Belsa) Ocampo
787-555-0148
bocampo@kestrelwing.example

Target Market(s)

finance and pharmaceutical companies

Industry/Entity Type

Business

Contact Information for Business Card

modern, edgy colorful and playfull like our logo

Requirements
Must have
• company logo
• name
• tel
• email

```html
<!DOCTYPE html>
<html lang="en">
<head>
<meta charset="utf-8">
<title>Kestrel Integrated Communications – Business Card</title>
<link rel="stylesheet" href="https://fonts.googleapis.com/css2?family=Source+Sans+3:wght@400;600&display=swap">
<style>
  :root {
    --backdrop: #8f8f8f;
    --card-light: #f1f1f0;
    --card-dark: #35290c;
    --accent: #cf4d1c;
    --ink: #2e2a22;
    --muted: #5b5b5b;
    --rule: #b9b9b9;
    --paper: #f2f2f2;
  }
  * { box-sizing: border-box; margin: 0; padding: 0; }
  html, body {
    width: 1105px; height: 1200px; overflow: hidden;
    background: var(--backdrop);
    font-family: "Source Sans 3", "Myriad Pro", Arial, sans-serif;
  }
  .sheet {
    width: 1105px; height: 1200px;
    display: flex; flex-direction: column; align-items: center; justify-content: center;
    gap: 80px;
  }
  .card { position: relative; width: 880px; height: 500px; overflow: hidden; }

  /* Front */
  .card--front { background: var(--card-light); }
  .card__band {
    position: absolute; left: 0; right: 0; bottom: 0; height: 38px;
    background: var(--accent); border-top: 4px solid var(--card-dark);
  }
  .wordmark {
    position: absolute; display: flex; align-items: center; gap: 14px;
    font-weight: 600; letter-spacing: 0.06em;
  }
  .card--front .wordmark {
    left: 90px; top: 205px; font-size: 52px; color: var(--card-dark);
  }
  .wordmark__dot { width: 22px; height: 22px; border-radius: 50%; background: var(--accent); }
  .card__divider {
    position: absolute; left: 456px; top: 98px; width: 1px; height: 228px; background: var(--rule);
  }
  .contact { position: absolute; left: 512px; top: 104px; }
  .contact__name { font-size: 30px; font-weight: 600; color: var(--accent); line-height: 1.15; }
  .contact__title { font-size: 22px; font-weight: 400; color: var(--ink); margin-top: 4px; }
  .contact__address { font-size: 22px; color: var(--muted); margin-top: 26px; line-height: 1.45; }
  .contact__list { list-style: none; margin-top: 10px; }
  .contact__item {
    display: flex; align-items: center; gap: 12px;
    font-size: 22px; color: var(--muted); line-height: 1.6; white-space: nowrap;
  }
  .contact__icon { width: 18px; height: 18px; fill: var(--accent); flex: none; }

  /* Back */
  .card--back { background: var(--card-dark); }
  .card--back .wordmark {
    left: 0; right: 0; top: 195px; justify-content: center;
    font-size: 70px; color: var(--paper);
  }
  .card--back .wordmark__dot { width: 28px; height: 28px; }
  .card__url {
    position: absolute; left: 0; right: 0; top: 418px; text-align: center;
    font-size: 22px; letter-spacing: 0.32em; color: var(--paper);
  }
</style>
</head>
<body>
<main class="sheet">
  <section class="card card--front" aria-label="Card front">
    <div class="wordmark"><span class="wordmark__name">KESTREL</span><span class="wordmark__dot"></span></div>
    <div class="card__divider"></div>
    <div class="contact">
      <h1 class="contact__name">Maribelsa Ocampo</h1>
      <p class="contact__title">CEO/Founder</p>
      <p class="contact__address">Bahía Serena<br>tropical island office</p>
      <ul class="contact__list">
        <li class="contact__item">
          <svg class="contact__icon" viewBox="0 0 24 24" aria-hidden="true"><path d="M6.6 10.8a15.1 15.1 0 0 0 6.6 6.6l2.2-2.2a1 1 0 0 1 1-.25 11.4 11.4 0 0 0 3.6.57 1 1 0 0 1 1 1V20a1 1 0 0 1-1 1A17 17 0 0 1 3 4a1 1 0 0 1 1-1h3.5a1 1 0 0 1 1 1c0 1.25.2 2.45.57 3.57a1 1 0 0 1-.25 1z"/></svg>
          787-555-0148
        </li>
        <li class="contact__item">
          <svg class="contact__icon" viewBox="0 0 24 24" aria-hidden="true"><path d="M2 5h20v14H2z"/><path d="M2 5l10 8 10-8" stroke="var(--card-light)" stroke-width="1.6" fill="none"/></svg>
          bocampo@kestrelwing.example
        </li>
        <li class="contact__item">
          <svg class="contact__icon" viewBox="0 0 24 24" aria-hidden="true"><circle cx="12" cy="12" r="10"/><path d="M2 12h20M12 2c3 3 3 17 0 20M12 2c-3 3-3 17 0 20" stroke="var(--card-light)" stroke-width="1.4" fill="none"/></svg>
          www.kestrelwing.example
        </li>
      </ul>
    </div>
    <div class="card__band"></div>
  </section>

  <section class="card card--back" aria-label="Card back">
    <div class="wordmark"><span class="wordmark__name">KESTREL</span><span class="wordmark__dot"></span></div>
    <p class="card__url">www.kestrelwing.example</p>
  </section>
</main>
</body>
</html>
```